Business Card Design

We are a commercial real estate brokerage in San Francisco, leasing office buildings downtown.
I would like a clean, elegant look. Simple but powerful .

Industry/Entity Type

Business

Contact Information for Business Card

Colin Farrow
lic# 07281549
415.555.0172
colin@tarvo-commercial.example
tarvo-commercial.example

```html
<!DOCTYPE html>
<html lang="en">
<head>
<meta charset="utf-8">
<title>Tarvo Commercial – Business Card</title>
<link rel="stylesheet" href="https://fonts.googleapis.com/css2?family=Carlito:wght@400;700&display=swap">
<style>
  :root {
    --card-white: #ffffff;
    --band-dark: #221a24;
    --accent-orange: #f7931e;
    --ink-dark: #2b2b2b;
    --text-light: #ffffff;
  }
  * { margin: 0; padding: 0; box-sizing: border-box; }
  html, body {
    width: 1200px;
    height: 687px;
    overflow: hidden;
    background: var(--card-white);
  }
  .card {
    position: relative;
    width: 1200px;
    height: 687px;
    background: var(--card-white);
    font-family: "Carlito", "Calibri", sans-serif;
  }
  .brand {
    position: absolute;
    top: 52px;
    left: 0;
    width: 1200px;
    display: flex;
    justify-content: center;
    align-items: center;
    gap: 34px;
  }
  .brand-mark {
    width: 150px;
    height: 150px;
    background: var(--ink-dark);
  }
  .brand-name {
    color: var(--ink-dark);
    font-weight: 700;
    line-height: 0.95;
    text-transform: uppercase;
  }
  .brand-name .primary { display: block; font-size: 120px; letter-spacing: 2px; }
  .brand-name .secondary { display: block; font-size: 52px; letter-spacing: 3px; }
  .agent-name {
    position: absolute;
    top: 300px;
    left: 0;
    width: 1200px;
    text-align: center;
    color: var(--accent-orange);
    font-weight: 700;
    font-size: 42px;
  }
  .contact-band {
    position: absolute;
    left: 0;
    top: 365px;
    width: 1200px;
    height: 322px;
    background: var(--band-dark);
  }
  .contact-item {
    position: absolute;
    display: flex;
    align-items: center;
    gap: 40px;
    color: var(--text-light);
    font-weight: 700;
    font-size: 34px;
  }
  .contact-icon {
    width: 82px;
    height: 82px;
    background: var(--accent-orange);
    display: flex;
    align-items: center;
    justify-content: center;
    flex-shrink: 0;
  }
  .contact-icon svg { width: 54px; height: 54px; }
  .licence-tag {
    color: var(--band-dark);
    font-size: 32px;
    font-weight: 700;
  }
  .item-licence { left: 50px; top: 432px; }
  .item-phone   { left: 50px; top: 569px; }
  .item-email   { left: 488px; top: 428px; gap: 28px; }
  .item-web     { left: 488px; top: 565px; gap: 28px; }
</style>
</head>
<body>
<div class="card">
  <header class="brand">
    <div class="brand-mark"></div>
    <div class="brand-name">
      <span class="primary">Tarvo</span>
      <span class="secondary">Commercial</span>
    </div>
  </header>

  <p class="agent-name">Colin Farrow</p>

  <section class="contact-band"></section>

  <div class="contact-item item-licence">
    <div class="contact-icon"><span class="licence-tag">Lic#</span></div>
    <span>07281549</span>
  </div>

  <div class="contact-item item-phone">
    <div class="contact-icon">
      <svg viewBox="0 0 24 24" aria-hidden="true">
        <path fill="#221a24" d="M6.6 10.8c1.4 2.8 3.8 5.1 6.6 6.6l2.2-2.2c.3-.3.7-.4 1-.2 1.1.4 2.3.6 3.6.6.6 0 1 .4 1 1V20c0 .6-.4 1-1 1C10.6 21 3 13.4 3 4c0-.6.4-1 1-1h3.5c.6 0 1 .4 1 1 0 1.3.2 2.5.6 3.6.1.3 0 .7-.2 1L6.6 10.8z"/>
      </svg>
    </div>
    <span>415.555.0172</span>
  </div>

  <div class="contact-item item-email">
    <div class="contact-icon">
      <svg viewBox="0 0 24 24" aria-hidden="true">
        <rect x="2" y="5" width="20" height="14" fill="none" stroke="#221a24" stroke-width="1.8"/>
        <path d="M2 5l10 8 10-8M2 19l7.5-7M22 19l-7.5-7" fill="none" stroke="#221a24" stroke-width="1.8"/>
      </svg>
    </div>
    <span>colin@tarvo-commercial.example</span>
  </div>

  <div class="contact-item item-web">
    <div class="contact-icon">
      <svg viewBox="0 0 24 24" aria-hidden="true">
        <g fill="none" stroke="#221a24" stroke-width="1.6">
          <circle cx="12" cy="12" r="9"/>
          <ellipse cx="12" cy="12" rx="4" ry="9"/>
          <path d="M3 12h18M4.5 7.5h15M4.5 16.5h15"/>
        </g>
      </svg>
    </div>
    <span>www.tarvo-commercial.example</span>
  </div>
</div>
</body>
</html>
```